New Web Design Project

you can visit www.solano-arepa.com and www.instagram.com\solanoarepa

www.elnopalito.co
www.instagram.com\enpt.co

combining this 2 business into one company website

### 1. **Home Page:**
- **Company Overview:** Briefly introduce Solano Arepa, highlight your mission and values.
- **Navigation Menu:** Links to About Us, Events, Catering, Menu, and Contact Us.
- **Dynamic Banner:** Showcase specials, events, and new updates.

### 2. **About Us Page:**
- **History:** Share your story, how you started, and your journey.
- **Team:** Introduce your key team members with photos and bios.

### 3. **Events Page:**
- **Dynamic Calendar:** Integrate Google Calendar to showcase events and schedules.
- **Event Details:** Detailed descriptions of upcoming events with images and RSVP options.

### 4. **Catering Page:**
- **Booking Form:** A user-friendly form for booking catering services.
- **Packages & Pricing:** Clearly list your catering packages and pricing.
- **Testimonials:** Showcase positive reviews from previous clients.

### 5. **Menu Page:**
- **Online Order:** Embed or redirect to your Square online order menu for easy access.
- **Menu Sections:** Categorize your menu items (e.g., Appetizers, Main Course, Desserts).

### 6. **Contact Us Page:**
- **Contact Form:** Simple form for inquiries and feedback.
- **Location & Hours:** Display your location on Google Maps and list your operating hours.
- **Social Media Links:** Integrate links to your Instagram and other social platforms.

### 7. **Responsive Design:**
- Ensure the website is mobile-friendly and responsive on all devices.

### 8. **SEO Optimization:**
- Use relevant keywords and meta tags to improve search engine ranking. optimize seo and google analytics , google reviews embedded

### 9. **Social Media Integration:**
- Add social media icons that link directly to your Instagram and other platforms.

### 10. **Security:**
- Ensure your website has SSL certification

```html
<!DOCTYPE html>
<html lang="en">
<head>
<meta charset="utf-8">
<title>El Nopalito Grill &amp; Solano Arepa</title>
<link rel="stylesheet" href="https://fonts.googleapis.com/css2?family=Bebas+Neue&family=Poppins:wght@400;500;600&family=Mr+Dafoe&display=swap">
<style>
:root{
  --ink:#222324;
  --ink-2:#2c2d2f;
  --paper:#f6f6f5;
  --white:#ffffff;
  --orange:#f7931e;
  --red:#d8232a;
  --muted:#d9d9d9;
  --text:#1d1d1d;
}
*{margin:0;padding:0;box-sizing:border-box}
html,body{width:1200px;height:3922px;overflow:hidden;background:var(--paper)}
body{font-family:"Poppins",sans-serif;color:var(--text)}
.page{position:relative;width:1200px;height:3922px;overflow:hidden}
.abs{position:absolute}
.display{font-family:"Bebas Neue",sans-serif;font-weight:400;letter-spacing:.5px}
.script{font-family:"Mr Dafoe",cursive;color:var(--red);font-size:34px;line-height:1}
.btn{position:absolute;display:flex;align-items:center;justify-content:center;font-family:"Bebas Neue",sans-serif;font-size:15px;letter-spacing:.6px;color:var(--ink)}
.btn--solid{background:var(--orange)}
.btn--ghost{border:1.5px solid var(--white);color:var(--white)}
.btn--ghost-orange{border:1.5px solid var(--orange);color:var(--orange)}
.edge{position:absolute;left:0;width:1200px;height:24px}
.arrow{position:absolute;width:30px;height:20px}
.arrow path{stroke:var(--white);stroke-width:2;fill:none}

/* sections */
.hero{left:0;top:0;width:1200px;height:612px;background:radial-gradient(ellipse at 55% 45%,#8a5a22 0%,#5a3718 35%,#35271f 70%,#262221 100%)}
.hero__shade{left:0;top:0;width:1200px;height:612px;background:rgba(20,18,18,.35)}
.nav{left:99px;top:50px;display:flex;gap:31px;font-size:12px;color:var(--white);letter-spacing:.3px}
.logo{font-family:"Bebas Neue",sans-serif;color:var(--red);font-size:34px;line-height:1;text-align:center}
.hero__title{left:0;top:232px;width:1200px;text-align:center;color:var(--white);font-size:66px;line-height:65px}
.hero__lead{left:0;top:384px;width:1200px;text-align:center;color:var(--white);font-size:12.5px;line-height:19px}

.light{background:linear-gradient(135deg,#fbfbfa 0%,#f1f1f0 40%,#fafaf9 60%,#eeeeed 100%)}
.dark{background:var(--ink)}
.about{left:0;top:606px;width:1200px;height:590px}
.about__title{left:99px;top:745px;font-size:50px;line-height:56px;color:var(--text)}
.about__copy{left:99px;top:866px;width:430px;font-size:11px;line-height:16.8px;color:var(--text)}
.about__copy p+p{margin-top:13px}
.photo{position:absolute}

.section-head{left:0;width:1200px;text-align:center}
.section-title{font-size:50px;line-height:1}
.menu{left:0;top:1186px;width:1200px;height:554px}
.menu-card{position:absolute;top:1356px;width:238px}
.menu-card__img{width:238px;height:213px}
.menu-card__label{margin-top:15px;text-align:center;color:var(--white);font-weight:600;font-size:18px;letter-spacing:.3px}

.catering{left:0;top:1734px;width:1200px;height:600px}
.cater-card{position:absolute;top:1994px;width:322px;height:246px;overflow:hidden}
.cater-card__shade{position:absolute;left:0;bottom:0;width:100%;height:55%;background:linear-gradient(to top,rgba(15,15,15,.85),rgba(15,15,15,0))}
.cater-card__name{position:absolute;left:16px;bottom:24px;color:var(--white);font-weight:600;font-size:18.5px;line-height:24px}
.cater-card__price{font-family:"Bebas Neue",sans-serif;font-size:12px;font-weight:400;margin-top:6px;letter-spacing:.3px}

.reviews{left:0;top:2328px;width:1200px;height:540px}
.review{position:absolute;top:2534px;width:490px;height:235px;background:var(--ink-2);padding:39px 20px 0}
.review__head{display:flex;align-items:center;gap:12px}
.avatar{width:42px;height:42px;border-radius:50%;background:linear-gradient(135deg,#cfcfcf,#8d8d8d);border:2px solid #e8e8e8}
.review__name{font-family:"Bebas Neue",sans-serif;color:var(--white);font-size:12px;letter-spacing:.4px;line-height:1.1}
.review__role{color:var(--orange);font-size:11px}
.review__quote{position:absolute;right:26px;top:30px;font-family:"Bebas Neue",sans-serif;font-size:86px;line-height:1;color:transparent;-webkit-text-stroke:2px var(--orange)}
.stars{margin-top:12px;color:var(--orange);font-size:17px;letter-spacing:3px}
.review__text{margin-top:6px;color:var(--white);font-size:11px;line-height:16.6px}

.events{left:0;top:2862px;width:1200px;height:670px}
.event{position:absolute;top:3067px;width:322px}
.event__img{width:322px;height:247px}
.event__title{margin-top:14px;font-weight:600;font-size:18.5px;line-height:24px;color:var(--text)}
.event__meta{margin-top:7px;display:flex;align-items:center;gap:6px;color:var(--orange);font-family:"Bebas Neue",sans-serif;font-size:10.5px;letter-spacing:.3px}
.event__meta svg{width:12px;height:12px}

.footer{left:0;top:3524px;width:1200px;height:398px}
.footer__col{position:absolute;top:3641px;color:var(--white);font-size:12px;line-height:25px}
.footer__heading{font-family:"Bebas Neue",sans-serif;font-size:16px;letter-spacing:.4px;margin-bottom:2px}
.hours{line-height:21px}
.hours span{display:block}
.hours .gap{margin-top:4px}
.contact-row{display:flex;gap:10px;align-items:flex-start;line-height:19px;margin-bottom:12px}
.contact-row i{flex:none;width:16px;height:16px;border-radius:50%;background:var(--orange);margin-top:2px;display:flex;align-items:center;justify-content:center}
.field{left:99px;top:3721px;width:274px;height:35px;border:1px solid #8a8a8a;color:#9a9a9a;font-size:9px;padding:11px 10px}
.divider{left:99px;top:3853px;width:1001px;height:1px;background:#6a6a6a}
.copyright{left:99px;top:3880px;color:var(--white);font-size:11.5px}
.social{left:981px;top:3878px;display:flex;gap:8px}
.social span{width:22px;height:22px;border-radius:50%;border:1.5px solid var(--red)}
</style>
</head>
<body>
<div class="page">

  <!-- HERO -->
  <section class="abs hero" role="img" aria-label="Close-up of roasted grilled meat being carved on a table"></section>
  <div class="abs hero__shade"></div>
  <nav class="abs nav"><span>ABOUT US</span><span>MENU</span><span>CATERING</span><span>EVENTS</span></nav>
  <div class="abs logo" style="left:500px;top:44px;width:200px">EL NOPALITO GRILL</div>
  <div class="btn btn--ghost-orange" style="left:867px;top:32px;width:112px;height:30px">ORDER NOW</div>
  <div class="btn btn--solid" style="left:988px;top:32px;width:112px;height:30px">CONTACT US</div>
  <svg class="arrow" style="left:57px;top:309px" viewBox="0 0 30 20"><path d="M28 10H3M11 2L3 10l8 8"/></svg>
  <svg class="arrow" style="left:1112px;top:309px" viewBox="0 0 30 20"><path d="M2 10h25M19 2l8 8-8 8"/></svg>
  <h1 class="abs display hero__title">CELEBRATE WITH FLAVOR,<br>CELEBRATE WITH US.</h1>
  <p class="abs hero__lead">Let us make your event unforgettable. Lorem Ipsum is simply<br>dummy text of the printing and typesetting industry.</p>
  <div class="btn btn--ghost" style="left:460px;top:440px;width:134px;height:30px">EXPLORE THE MENU</div>
  <div class="btn btn--solid" style="left:603px;top:440px;width:136px;height:30px">BOOK CATERING</div>

  <!-- ABOUT -->
  <section class="abs about light"></section>
  <svg class="edge" style="top:592px" viewBox="0 0 1200 24" preserveAspectRatio="none"><path fill="#fafaf9" d="M0,12 40,8 70,14 110,6 150,12 190,9 230,15 270,7 310,11 350,5 390,13 430,9 470,14 510,6 550,10 590,4 630,12 670,8 710,15 750,7 790,11 830,5 870,13 910,9 950,14 990,6 1030,11 1070,8 1110,14 1150,7 1200,10 1200,24 0,24Z"/></svg>
  <div class="abs script" style="left:97px;top:704px">About Us</div>
  <h2 class="abs display about__title">ROOTED IN FAMILY,<br>CRAFTED WITH LOVE.</h2>
  <div class="abs about__copy">
    <p>At Solano Arepa and El Nopalito, we believe great food brings people together. From our hand-crafted empanadas to our family-style dishes, every bite tells a story of tradition, passion, and community. Whether you're celebrating a milestone or just enjoying a meal with loved ones, our mission is to deliver unforgettable flavors that make every moment special."</p>
    <p>Lorem Ipsum is simply dummy text of the printing and typesetting industry. Lorem Ipsum has been the industry's standard dummy text ever since the 1500s, when an unknown printer took a galley of type and scrambled it to make a type specimen book.</p>
  </div>
  <div class="btn btn--solid" style="left:99px;top:1049px;width:172px;height:31px">LEARN MORE ABOUT US</div>
  <div class="photo" role="img" aria-label="Platter of grilled meats, fried pork and a fried egg" style="left:647px;top:719px;width:217px;height:288px;background:linear-gradient(160deg,#6b3a1c,#a0622a 45%,#d7b47a 70%,#5a2d18)"></div>
  <div class="photo" role="img" aria-label="Overhead view of a large party platter of skewers and grilled meats" style="left:883px;top:751px;width:217px;height:288px;background:linear-gradient(200deg,#9b4a22,#c2722f 40%,#e0a640 60%,#6d3319)"></div>

  <!-- MENU -->
  <section class="abs menu dark"></section>
  <svg class="edge" style="top:1174px" viewBox="0 0 1200 24" preserveAspectRatio="none"><path fill="#222324" d="M0,10 45,14 85,7 125,12 165,5 205,13 245,9 285,15 325,8 365,12 405,6 445,14 485,9 525,13 565,5 605,11 645,8 685,14 725,6 765,12 805,9 845,15 885,7 925,11 965,5 1005,13 1045,9 1085,14 1125,6 1165,12 1200,9 1200,24 0,24Z"/></svg>
  <div class="abs section-head" style="top:1246px"><span class="script">Our Menu</span></div>
  <h2 class="abs display section-head section-title" style="top:1283px;color:var(--white)">OUR DELICIOUS OFFERINGS</h2>
  <svg class="arrow" style="left:57px;top:1468px" viewBox="0 0 30 20"><path d="M28 10H3M11 2L3 10l8 8"/></svg>
  <svg class="arrow" style="left:1112px;top:1468px" viewBox="0 0 30 20"><path d="M2 10h25M19 2l8 8-8 8"/></svg>
  <div class="menu-card" style="left:99px"><div class="menu-card__img" role="img" aria-label="Bowl of crispy chopped pork" style="background:linear-gradient(150deg,#e8a33a,#c9702c 50%,#f0c07a)"></div><div class="menu-card__label">CRISPY</div></div>
  <div class="menu-card" style="left:353px"><div class="menu-card__img" role="img" aria-label="Grilled skewers with rice on a plate" style="background:linear-gradient(150deg,#f2ede6,#d8cfc2 40%,#7a4a2c 70%,#c23a3a)"></div><div class="menu-card__label">GRILLED</div></div>
  <div class="menu-card" style="left:608px"><div class="menu-card__img" role="img" aria-label="Bowl of ramen on a dark background" style="background:radial-gradient(circle at 50% 50%,#b98a55 0%,#5a4332 30%,#1c1c1c 55%)"></div><div class="menu-card__label">RAMEN</div></div>
  <div class="menu-card" style="left:862px"><div class="menu-card__img" role="img" aria-label="Baked empanada on a white plate" style="background:linear-gradient(160deg,#dfe4e6,#f4f1ea 40%,#e6b35a 65%,#c9572f)"></div><div class="menu-card__label">BAKED EMPANADA</div></div>
  <div class="btn btn--solid" style="left:513px;top:1639px;width:174px;height:30px">EXPLORE ALL MENU</div>

  <!-- CATERING -->
  <section class="abs catering light"></section>
  <svg class="edge" style="top:1722px" viewBox="0 0 1200 24" preserveAspectRatio="none"><path fill="#fbfbfa" d="M0,12 40,8 70,14 110,6 150,12 190,9 230,15 270,7 310,11 350,5 390,13 430,9 470,14 510,6 550,10 590,4 630,12 670,8 710,15 750,7 790,11 830,5 870,13 910,9 950,14 990,6 1030,11 1070,8 1110,14 1150,7 1200,10 1200,24 0,24Z"/></svg>
  <div class="abs script" style="left:97px;top:1845px">Catering Items</div>
  <h2 class="abs display section-title" style="left:99px;top:1889px;color:var(--text)">CATERING SPECIALS</h2>
  <div class="btn btn--solid" style="left:978px;top:1869px;width:122px;height:30px">EXPLORE ALL</div>
  <div class="cater-card" style="left:99px"><div role="img" aria-label="Party tray of crispy pork, eggplant and green beans" style="position:absolute;inset:0;background:linear-gradient(170deg,#cfd6d2,#5b5553 35%,#6a7a3a 55%,#a25a2a)"></div><div class="cater-card__shade"></div><div class="cater-card__name">BAGNET Kare-Kare Party Tray</div></div>
  <div class="cater-card" style="left:439px"><div role="img" aria-label="Pork skewers on a banana leaf" style="position:absolute;inset:0;background:linear-gradient(160deg,#d8663a,#3f6b3a 35%,#4a2a22 60%,#c27a3a)"></div><div class="cater-card__shade"></div><div class="cater-card__name">Pork Skewers<br>(Filipino Style Pork BBQ)<div class="cater-card__price">CAD$79.99 - CAD$150.00</div></div></div>
  <div class="cater-card" style="left:778px"><div role="img" aria-label="Golden crispy pork knuckle with dipping sauce" style="position:absolute;inset:0;background:linear-gradient(160deg,#e9e0cf,#d99a4a 40%,#a5582a 65%,#4a2a1a)"></div><div class="cater-card__shade"></div><div class="cater-card__name">Crispy Pata</div></div>

  <!-- TESTIMONIALS -->
  <section class="abs reviews dark"></section>
  <svg class="edge" style="top:2316px" viewBox="0 0 1200 24" preserveAspectRatio="none"><path fill="#222324" d="M0,10 45,14 85,7 125,12 165,5 205,13 245,9 285,15 325,8 365,12 405,6 445,14 485,9 525,13 565,5 605,11 645,8 685,14 725,6 765,12 805,9 845,15 885,7 925,11 965,5 1005,13 1045,9 1085,14 1125,6 1165,12 1200,9 1200,24 0,24Z"/></svg>
  <div class="abs section-head" style="top:2410px"><span class="script">Testimonials</span></div>
  <h2 class="abs display section-head section-title" style="top:2449px;color:var(--white)">WHAT CLIENT SAYS</h2>
  <svg class="arrow" style="left:57px;top:2640px" viewBox="0 0 30 20"><path d="M28 10H3M11 2L3 10l8 8"/></svg>
  <svg class="arrow" style="left:1112px;top:2640px" viewBox="0 0 30 20"><path d="M2 10h25M19 2l8 8-8 8"/></svg>
  <article class="review" style="left:99px">
    <div class="review__head"><div class="avatar" role="img" aria-label="Client portrait"></div><div><div class="review__name">DANA REYES</div><div class="review__role">Cook</div></div></div>
    <div class="review__quote">”</div>
    <div class="stars">★★★★★</div>
    <p class="review__text">Lorem Ipsum is simply dummy text of the printing and typesetting industry. Lorem Ipsum has been the industry's standard dummy text ever since the 1500s, when an unknown printer took a galley of type and scrambled it to make a type specimen book. Lorem Ipsum is simply dummy text of the printing and typesetting industry.</p>
  </article>
  <article class="review" style="left:608px">
    <div class="review__head"><div class="avatar" role="img" aria-label="Client portrait"></div><div><div class="review__name">DANA REYES</div><div class="review__role">Cook</div></div></div>
    <div class="review__quote">”</div>
    <div class="stars">★★★★★</div>
    <p class="review__text">Lorem Ipsum is simply dummy text of the printing and typesetting industry. Lorem Ipsum has been the industry's standard dummy text ever since the 1500s, when an unknown printer took a galley of type and scrambled it to make a type specimen book. Lorem Ipsum is simply dummy text of the printing and typesetting industry.</p>
  </article>

  <!-- EVENTS -->
  <section class="abs events light"></section>
  <svg class="edge" style="top:2850px" viewBox="0 0 1200 24" preserveAspectRatio="none"><path fill="#fbfbfa" d="M0,12 40,8 70,14 110,6 150,12 190,9 230,15 270,7 310,11 350,5 390,13 430,9 470,14 510,6 550,10 590,4 630,12 670,8 710,15 750,7 790,11 830,5 870,13 910,9 950,14 990,6 1030,11 1070,8 1110,14 1150,7 1200,10 1200,24 0,24Z"/></svg>
  <div class="abs section-head" style="top:2937px"><span class="script">Come &amp; Join</span></div>
  <h2 class="abs display section-head section-title" style="top:2984px;color:var(--text)">LATEST EVENTS</h2>
  <div class="event" style="left:99px">
    <div class="event__img" role="img" aria-label="Party tray of crispy pork and vegetables" style="background:linear-gradient(170deg,#cfd6d2,#5b5553 35%,#6a7a3a 55%,#a25a2a)"></div>
    <div class="event__title">Lorem ipsum dolor sit amet, consectetur adipiscing elit.</div>
    <div class="event__meta"><svg viewBox="0 0 12 12"><rect x="1" y="2" width="10" height="9" fill="none" stroke="#f7931e"/><path d="M1 5h10M4 1v2M8 1v2" stroke="#f7931e"/></svg>20 DEC, 2024 &nbsp;&nbsp;<svg viewBox="0 0 12 12"><circle cx="6" cy="6" r="5" fill="none" stroke="#f7931e"/><path d="M6 3v3l2 1" stroke="#f7931e" fill="none"/></svg>12:30 AM - 15:00 AM</div>
  </div>
  <div class="event" style="left:439px">
    <div class="event__img" role="img" aria-label="Pork skewers on a banana leaf" style="background:linear-gradient(160deg,#d8663a,#3f6b3a 35%,#4a2a22 60%,#c27a3a)"></div>
    <div class="event__title">Lorem ipsum dolor sit amet, consectetur adipiscing elit.</div>
    <div class="event__meta"><svg viewBox="0 0 12 12"><rect x="1" y="2" width="10" height="9" fill="none" stroke="#f7931e"/><path d="M1 5h10M4 1v2M8 1v2" stroke="#f7931e"/></svg>20 DEC, 2024 &nbsp;&nbsp;<svg viewBox="0 0 12 12"><circle cx="6" cy="6" r="5" fill="none" stroke="#f7931e"/><path d="M6 3v3l2 1" stroke="#f7931e" fill="none"/></svg>12:30 AM - 15:00 AM</div>
  </div>
  <div class="event" style="left:778px">
    <div class="event__img" role="img" aria-label="Crispy pork knuckle with dipping sauce" style="background:linear-gradient(160deg,#e9e0cf,#d99a4a 40%,#a5582a 65%,#4a2a1a)"></div>
    <div class="event__title">Lorem ipsum dolor sit amet, consectetur adipiscing elit.</div>
    <div class="event__meta"><svg viewBox="0 0 12 12"><rect x="1" y="2" width="10" height="9" fill="none" stroke="#f7931e"/><path d="M1 5h10M4 1v2M8 1v2" stroke="#f7931e"/></svg>20 DEC, 2024 &nbsp;&nbsp;<svg viewBox="0 0 12 12"><circle cx="6" cy="6" r="5" fill="none" stroke="#f7931e"/><path d="M6 3v3l2 1" stroke="#f7931e" fill="none"/></svg>12:30 AM - 15:00 AM</div>
  </div>
  <div class="btn btn--solid" style="left:539px;top:3425px;width:122px;height:31px">VIEW ALL</div>

  <!-- FOOTER -->
  <footer class="abs footer dark"></footer>
  <svg class="edge" style="top:3512px" viewBox="0 0 1200 24" preserveAspectRatio="none"><path fill="#222324" d="M0,10 45,14 85,7 125,12 165,5 205,13 245,9 285,15 325,8 365,12 405,6 445,14 485,9 525,13 565,5 605,11 645,8 685,14 725,6 765,12 805,9 845,15 885,7 925,11 965,5 1005,13 1045,9 1085,14 1125,6 1165,12 1200,9 1200,24 0,24Z"/></svg>
  <div class="abs logo" style="left:99px;top:3640px;width:274px;font-size:40px">EL NOPALITO GRILL</div>
  <div class="abs field">Email</div>
  <div class="btn btn--solid" style="left:99px;top:3771px;width:274px;height:35px">SUBSCRIBE</div>
  <div class="footer__col" style="left:454px">
    <div class="footer__heading">QUICK LINKS</div>
    <div>About Us</div><div>Menu</div><div>Catering</div><div>Events</div><div>Contact US</div>
  </div>
  <div class="footer__col hours" style="left:603px">
    <div class="footer__heading" style="line-height:25px">OPENING HOURS</div>
    <span>Monday 10:00 a.m. - 10:00 p.m.</span>
    <span>Wednesday &amp; Thursday &amp; Sunday</span>
    <span class="gap">11:30 a.m. - 8:00 p.m.</span>
    <span>Friday &amp; Saturday</span>
    <span class="gap">11:30 a.m. - 9:30 p.m.</span>
    <span>Tuesday - Closed</span>
  </div>
  <div class="footer__col" style="left:896px;width:210px">
    <div class="footer__heading" style="margin-bottom:6px">CONTACT US</div>
    <div class="contact-row"><i><svg width="9" height="9" viewBox="0 0 10 10"><path d="M2 1l2 2-1 1.5a6 6 0 0 0 2.5 2.5L7 6l2 2-1.5 1.5C4.5 9 1 5.5.5 2.5Z" fill="#fff"/></svg></i><span>(365) 555-0148</span></div>
    <div class="contact-row"><i><svg width="9" height="9" viewBox="0 0 10 10"><rect x="1" y="2" width="8" height="6" fill="none" stroke="#fff"/><path d="M1 2l4 3 4-3" stroke="#fff" fill="none"/></svg></i><span>hello@nopalitogrill.co</span></div>
    <div class="contact-row"><i><svg width="9" height="9" viewBox="0 0 10 10"><path d="M5 9.5S1.5 6 1.5 4a3.5 3.5 0 0 1 7 0C8.5 6 5 9.5 5 9.5Z" fill="#fff"/><circle cx="5" cy="4" r="1.2" fill="#f7931e"/></svg></i><span>El Nopalito Grill<br>418 Maple Crest Road<br>Niagara Falls, Ontario L2G 0A1</span></div>
  </div>
  <div class="abs divider"></div>
  <div class="abs copyright">© Copyright All Right Reserved 2024</div>
  <div class="abs social"><span></span><span></span><span></span><span></span></div>

</div>
</body>
</html>
```